New Chartered Accounting Practice Needs Stationery Design

I need a new set of stationery including letterhead, business cards, envelopes and with compliments slips for a new Chartered Accounting Practice based in Melbourne, Victoria, Australia called "Martin K. Ashbury, Chartered Accountant".
I will be providing Taxation Services, Accounting Services, Self-Managed Superannuation Fund Consulting and general consulting advice to small and medium business enterprises. I would like to see designs that use the colour blue. The final design should communicate trust, technical expertise and security.
Target Market(s)
English speaking, Australians. Proprietors of small and medium businesses - aged 30-65. Fellow professionals - lawyers, investment consultants, other accountants. Retirees - aged 60 and over
Industry/Entity Type
Business
Look and feel

```html
<!DOCTYPE html>
<html lang="en">
<head>
<meta charset="utf-8">
<title>Martin K. Ashbury, Chartered Accountant – Presentation Folder</title>
<link rel="stylesheet" href="https://fonts.googleapis.com/css2?family=Cinzel:wght@400&family=PT+Sans:wght@400&display=swap">
<style>
  :root {
    --backdrop: #ebebeb;
    --navy: #22305a;
    --navy-mid: #1f2c52;
    --navy-deep: #1a2648;
    --fold: #4a5a82;
    --white: #ffffff;
    --soft-white: #e3e7f0;
  }
  html, body {
    margin: 0;
    padding: 0;
    width: 1200px;
    height: 900px;
    overflow: hidden;
    background: var(--backdrop);
  }
  .canvas {
    position: relative;
    width: 1200px;
    height: 900px;
  }
  .folder {
    position: absolute;
    left: 80px;
    top: 88px;
    width: 1040px;
    height: 720px;
    box-shadow: 0 2px 6px rgba(0, 0, 0, 0.18);
  }
  .folder-surface {
    position: absolute;
    inset: 0;
    background:
      radial-gradient(ellipse at 30% 20%, rgba(255, 255, 255, 0.05) 0%, rgba(255, 255, 255, 0) 60%),
      radial-gradient(ellipse at 75% 80%, rgba(255, 255, 255, 0.04) 0%, rgba(255, 255, 255, 0) 55%),
      linear-gradient(180deg, var(--navy) 0%, var(--navy-mid) 55%, var(--navy-deep) 100%);
  }
  .folder-fold {
    position: absolute;
    left: 519px;
    top: 0;
    width: 1px;
    height: 100%;
    background: var(--fold);
  }
  .contact-block {
    position: absolute;
    left: 38px;
    top: 629px;
    margin: 0;
    font-family: "PT Sans", Arial, sans-serif;
    font-size: 11px;
    line-height: 12px;
    letter-spacing: 0.2px;
    color: var(--white);
    font-style: normal;
  }
  .contact-block span { display: block; }
  .brand-mark {
    position: absolute;
    right: 40px;
    top: 37px;
    width: 118px;
    height: 118px;
    background: var(--white);
    display: flex;
    align-items: center;
    justify-content: center;
  }
  .brand-mark-name {
    font-family: "Cinzel", Georgia, serif;
    font-size: 19px;
    color: var(--navy-mid);
    letter-spacing: 0.5px;
  }
  .signature {
    position: absolute;
    right: 40px;
    top: 646px;
    text-align: right;
  }
  .signature-name {
    margin: 0;
    font-family: "Cinzel", Georgia, serif;
    font-weight: 400;
    font-size: 21px;
    line-height: 24px;
    letter-spacing: 1px;
    color: var(--white);
    border-bottom: 1px solid var(--white);
    padding-bottom: 2px;
  }
  .signature-title {
    margin: 3px 0 0;
    font-family: "PT Sans", Arial, sans-serif;
    font-size: 10.5px;
    letter-spacing: 1.5px;
    color: var(--soft-white);
  }
</style>
</head>
<body>
  <main class="canvas">
    <section class="folder">
      <div class="folder-surface" role="img" aria-label="Deep navy folder surface with a subtle tone-on-tone scalloped fan pattern"></div>
      <div class="folder-fold"></div>

      <address class="contact-block">
        <span>Office: 18 Larkspur Street, Kew VIC 3101</span>
        <span>Postal: PO Box 4409, Kew VIC 3101</span>
        <span>Phone: 0432 618 204</span>
        <span>Fax: (03) 9761 2250</span>
        <span>Email: martin.ashbury@ashburyca.com.au</span>
      </address>

      <div class="brand-mark">
        <span class="brand-mark-name">Ashbury</span>
      </div>

      <div class="signature">
        <h1 class="signature-name">MARTIN K. ASHBURY</h1>
        <p class="signature-title">CHARTERED ACCOUNTANT</p>
      </div>
    </section>
  </main>
</body>
</html>
```